Land Buying Company Needs Letterhead for Direct Mail Marketing to Land Owners

We are looking for a professional letterhead that we will be including in our direct mail marketing. We will be sending this to land owners who may be interested in selling or purchasing land.

The letterhead needs to be editable. Headers and footers would look nice, but we are open. We would want it to include our address, website, phone, and email info. For right now the address to use for design purposes would the following:

Address: 415 Bramwell Avenue #600
Dallas, TX 75219
Website - www.quillridgeacres.example
Email - info@quillridgeacres.example
Phone - 866-402-ACRE

I have attached our logo zip file that we just had done on Pixel Guild. Let me know what questions you have, and thank you.

```html
<!DOCTYPE html>
<html lang="en">
<head>
<meta charset="utf-8">
<title>Quill Ridge Acres Letterhead</title>
<link href="https://fonts.googleapis.com/css2?family=Montserrat:wght@400;500;600;700&family=Roboto:wght@400;500&family=Mrs+Saint+Delafield&display=swap" rel="stylesheet">
<style>
  :root {
    --stage: #e4e4e4;
    --paper: #f7f7f7;
    --forest: #3d5a1e;
    --leaf: #8dc63f;
    --ink: #333333;
    --muted: #8a8a8a;
    --body-text: #8f8f8f;
  }
  * { box-sizing: border-box; margin: 0; padding: 0; }
  html, body {
    width: 1110px;
    height: 1200px;
    overflow: hidden;
    background: var(--stage);
  }
  .letterhead {
    position: absolute;
    left: 127px;
    top: 0;
    width: 855px;
    height: 1200px;
    background: var(--paper);
    font-family: "Montserrat", sans-serif;
    color: var(--ink);
  }
  .header-band {
    position: absolute;
    top: 0;
    right: 0;
    width: 855px;
    height: 160px;
  }
  .brand {
    position: absolute;
    left: 46px;
    top: 46px;
    display: flex;
    align-items: center;
    gap: 14px;
  }
  .brand-dot {
    width: 56px;
    height: 56px;
    border-radius: 50%;
    background: var(--forest);
  }
  .brand-name {
    font-weight: 700;
    font-size: 29px;
    letter-spacing: 1px;
    color: var(--leaf);
    text-transform: uppercase;
  }
  .recipient {
    position: absolute;
    left: 87px;
    top: 268px;
  }
  .recipient .label {
    font-size: 16px;
    letter-spacing: 1px;
    margin-bottom: 9px;
  }
  .recipient .name {
    font-size: 14px;
    color: var(--leaf);
    margin-bottom: 8px;
  }
  .recipient .line {
    font-size: 11.5px;
    color: var(--muted);
    line-height: 19px;
  }
  .date {
    position: absolute;
    right: 86px;
    top: 268px;
    font-size: 12px;
    color: var(--muted);
  }
  .letter-body {
    position: absolute;
    left: 87px;
    top: 481px;
    width: 683px;
    font-size: 11.4px;
    line-height: 11.7px;
    color: var(--body-text);
    text-align: justify;
  }
  .letter-body p { margin-bottom: 11.7px; }
  .sign-off {
    position: absolute;
    left: 87px;
    top: 884px;
  }
  .signature {
    font-family: "Mrs Saint Delafield", cursive;
    font-size: 30px;
    color: var(--ink);
    line-height: 30px;
    margin-left: 4px;
  }
  .signer-name {
    font-size: 14px;
    margin-top: 8px;
  }
  .signer-role {
    font-size: 10.5px;
    color: var(--muted);
    margin-top: 3px;
  }
  .contact-list {
    position: absolute;
    left: 43px;
    top: 1121px;
    list-style: none;
    font-family: "Roboto", sans-serif;
    font-size: 14.5px;
    color: var(--forest);
  }
  .contact-list li {
    display: flex;
    align-items: center;
    gap: 8px;
    height: 17.5px;
  }
  .contact-list svg { width: 10px; height: 10px; fill: var(--leaf); }
  .contact-list .web-name { color: var(--leaf); }
  .office-address {
    position: absolute;
    right: 41px;
    top: 1138px;
    text-align: right;
    font-family: "Roboto", sans-serif;
    font-size: 14.5px;
    line-height: 17.5px;
    color: var(--forest);
  }
</style>
</head>
<body>
<main class="letterhead">
  <svg class="header-band" viewBox="0 0 855 160" role="img" aria-label="Green header band with pine tree and bird illustration">
    <path d="M470 0 C560 4 610 50 655 92 C690 120 720 124 760 118 L855 112 L855 0 Z" fill="var(--leaf)"/>
    <path d="M483 0 C565 6 612 48 660 88 C694 114 722 116 760 112 L855 104 L855 0 Z" fill="var(--forest)"/>
  </svg>

  <div class="brand">
    <div class="brand-dot"></div>
    <div class="brand-name">Quill Ridge Acres</div>
  </div>

  <section class="recipient">
    <div class="label">TO</div>
    <div class="name">Priya Nandakumar</div>
    <div class="line">Human Resources</div>
    <div class="line">Brightfield Systems Inc.</div>
    <div class="line">2207-B Larkmoor Road, Fenwick</div>
    <div class="line">F42 USA</div>
  </section>

  <div class="date">Friday, 01/01/2018</div>

  <article class="letter-body">
    <p>Lorem ipsum dolor sit amet, consectetuer adipiscing elit, sed diam nonummy nibh euismod tincidunt ut laoreet dolore magna aliquam erat volutpat. Ut wisi enim ad minim veniam, quis nostrud exerci tationmcorper suscipit lobortis nisl ut aliquip ex ea commodo consequat. Duis autem vel eum iriure dolor in hendrerit in vulputate velit esse molestie consequat, vel illum dolore eu feugiat nulla facilisis at vero eros et accumsan et iusto odio dignissim qui blandit praesent luptatum zzril delenit augue duis dolore te feugait nulla facilisi.</p>
    <p>Nam liber tempor cum soluta nobis eleifend option congue nihil imprdiet doming id quod mazim placerat facer possim assum. Typi non habent claritatem insitam;</p>
    <p>Est usus legentis in iis qui facit eorum claritatem.</p>
    <p>Investigationes demonstraverunt lectores legere me lius quod ii legunt saepius. Claritas est etiam processus dynamicus, qui sequitur mutationem consuetudium lectorum. Mirum est notare quam littera gothica, quam nunc putamus parum claram, anteposuerit litterarum formas humanitatis per seacula quarta decima et quinta decima. Eodem modo typi, qui nunc nobis videntur parum clari, fiant sollemnes in futurum.</p>
    <p>consectetuer adipiscing elit, sed diam nonummy nibh euismod tincidunt ut laoreet dolore magna aliquam erat volutpat. Ut wisi enim ad minim veniam, quis nostrud exerci tation ullamcorper suscipit lobortis nisl ut aliquip ex ea commodo consequat. Duis autem vel eum iriure dolor in hendrerit in vulputate velit esse molestie consequat, vel illum dolore eu feugiat nulla facilisis at vero eros et accumsan et iusto odio dignissim qui blandit praesent luptatum zzril delenit augue duis dolore te feugait nulla facilisi.</p>
    <p>Nam liber tempor cum soluta nobis eleifend option congue nihil imperdiet .</p>
  </article>

  <section class="sign-off">
    <div class="signature">daniel hartley</div>
    <div class="signer-name">Daniel Hartley</div>
    <div class="signer-role">Managing Director</div>
  </section>

  <ul class="contact-list">
    <li>
      <svg viewBox="0 0 10 10" aria-hidden="true"><path d="M2 0.5 L3.6 2.6 L2.7 3.7 C3.3 5 4.9 6.7 6.3 7.3 L7.4 6.4 L9.5 8 L8.3 9.5 C4.5 9 1 5.5 0.5 1.7 Z"/></svg>
      <span>866-402-ACRE</span>
    </li>
    <li>
      <svg viewBox="0 0 10 10" aria-hidden="true"><path d="M0.5 2 H9.5 V8.5 H0.5 Z M0.5 2 L5 5.6 L9.5 2" stroke="var(--paper)" stroke-width="0.8"/></svg>
      <span>info@quillridgeacres.example</span>
    </li>
    <li>
      <svg viewBox="0 0 10 10" aria-hidden="true"><circle cx="5" cy="5" r="4.5"/><path d="M0.5 5 H9.5 M5 0.5 C2.8 3 2.8 7 5 9.5 M5 0.5 C7.2 3 7.2 7 5 9.5" stroke="var(--paper)" stroke-width="0.7" fill="none"/></svg>
      <span>www.<span class="web-name">quillridgeacres</span>.example</span>
    </li>
  </ul>

  <address class="office-address" style="font-style: normal;">
    415 Bramwell Avenue #600<br>
    Dallas, TX 75219
  </address>
</main>
</body>
</html>
```